Larkspur Ridge Management - Business Cards

I need business cards. My current logo was designed by a designer at this site and I very much like and am happy with the results. I would like a business card that is trendy, unique, current yet professional. I deal with high net worth clients daily

Target Market(s)

Out of state investors looking to get into the rental market in Ohio

Industry/Entity Type

Property Management, Consulting

Contact Information for Business Card

Name, Title (Chief Financial Officer) office phone number (555) 817-3094 website address larkridgemgmt.example

Font styles to use
Sans Serif

Colors
0054AA
0677BA
7BADD7
CADEEF
E8F1F8
0094D4
00A9DD
6FCCEA
C7EBF8
E9F6FB
00AB8E
00BBA5
67D7C9
C6EFE9
E9F9F6

```html
<!DOCTYPE html>
<html lang="en">
<head>
<meta charset="utf-8">
<title>Larkspur Ridge Management – Business Cards</title>
<link rel="stylesheet" href="https://fonts.googleapis.com/css2?family=Montserrat:wght@400;500;700&display=swap">
<style>
  :root {
    --bg-top: #b0c9cc;
    --bg-bottom: #dcf9fa;
    --navy: #22345a;
    --navy-soft: #2e4468;
    --slate: #5a6a87;
    --red: #d0302f;
    --white: #ffffff;
    --ink: #22345a;
    --grey-text: #555b66;
  }
  * { box-sizing: border-box; margin: 0; padding: 0; }
  html, body { width: 1200px; height: 1200px; overflow: hidden; }
  body {
    background: linear-gradient(180deg, var(--bg-top) 0%, var(--bg-bottom) 100%);
    font-family: "Montserrat", Arial, sans-serif;
    position: relative;
  }
  .card {
    position: absolute;
    left: 240px;
    width: 720px;
    height: 412px;
    overflow: hidden;
  }
  .card-front { top: 150px; background: var(--navy); }
  .card-back { top: 640px; background: var(--white); box-shadow: 0 2px 8px rgba(40,70,80,0.12); }

  .front-decoration {
    position: absolute;
    left: 0; top: 110px;
    width: 300px; height: 302px;
    background: linear-gradient(160deg, rgba(90,106,135,0.45) 0%, rgba(46,68,104,0.35) 60%, rgba(208,48,47,0.12) 100%);
  }
  .front-mark {
    position: absolute;
    right: 56px; top: 168px;
    display: flex; align-items: center; gap: 14px;
  }
  .mark-square { width: 20px; height: 20px; background: var(--red); flex: none; }
  .mark-name {
    color: var(--white);
    font-weight: 700;
    font-size: 22px;
    line-height: 1.2;
    width: 230px;
    text-transform: uppercase;
    letter-spacing: 0.5px;
  }

  .back-mark {
    position: absolute;
    left: 80px; top: 160px;
    display: flex; align-items: center; gap: 14px;
  }
  .back-mark .mark-name { color: var(--navy); width: 220px; }

  .contact-block {
    position: absolute;
    left: 380px; top: 118px;
  }
  .person-name { font-weight: 700; font-size: 32px; color: var(--ink); line-height: 1; }
  .person-title { font-weight: 500; font-size: 13px; color: var(--grey-text); margin-top: 6px; }
  .contact-list { list-style: none; margin-top: 26px; }
  .contact-list li {
    display: flex; align-items: center; gap: 14px;
    font-size: 17px; color: var(--grey-text);
    margin-bottom: 10px;
  }
  .contact-list svg { width: 18px; height: 18px; flex: none; }
</style>
</head>
<body>
  <section class="card card-front">
    <div class="front-decoration" role="img" aria-label="Large faint house emblem decoration"></div>
    <div class="front-mark">
      <span class="mark-square"></span>
      <span class="mark-name">Larkspur Ridge Management</span>
    </div>
  </section>

  <section class="card card-back">
    <div class="back-mark">
      <span class="mark-square"></span>
      <span class="mark-name">Larkspur Ridge Management</span>
    </div>
    <div class="contact-block">
      <h1 class="person-name">Jordan Avery</h1>
      <p class="person-title">Chief Financial Officer</p>
      <ul class="contact-list">
        <li>
          <svg viewBox="0 0 24 24" aria-hidden="true"><path fill="var(--red)" d="M6.6 10.8c1.4 2.8 3.8 5.1 6.6 6.6l2.2-2.2c.3-.3.7-.4 1-.2 1.1.4 2.3.6 3.6.6.6 0 1 .4 1 1V20c0 .6-.4 1-1 1C10.6 21 3 13.4 3 4c0-.6.4-1 1-1h3.5c.6 0 1 .4 1 1 0 1.3.2 2.5.6 3.6.1.3 0 .7-.2 1l-2.3 2.2z"/></svg>
          <span>(555) 817-3094</span>
        </li>
        <li>
          <svg viewBox="0 0 24 24" aria-hidden="true" fill="none" stroke="var(--red)" stroke-width="1.8"><circle cx="12" cy="12" r="9"/><ellipse cx="12" cy="12" rx="4" ry="9"/><line x1="3" y1="12" x2="21" y2="12"/><line x1="4.5" y1="7.5" x2="19.5" y2="7.5"/><line x1="4.5" y1="16.5" x2="19.5" y2="16.5"/></svg>
          <span>www.larkridgemgmt.example</span>
        </li>
      </ul>
    </div>
  </section>
</body>
</html>
```